Business Card Design

TAX PREPARATION CO.
INCOME & SALES TAXES
ELECTRONIC FILING
ESTABLISHED IN 1993
Looking for a design with a lady at a table with a pen over a 1040 form looking puzzled and a bubble with wording I'm in over my head.

Business

FILEWELL PLUS INC

```html
<!DOCTYPE html>
<html lang="en">
<head>
<meta charset="UTF-8">
<title>Tax Preparation Co. – Business Card</title>
<link rel="stylesheet" href="https://fonts.googleapis.com/css2?family=Arimo:ital,wght@0,700;1,400;1,700&family=Source+Serif+4:opsz,wght@8..60,700&display=swap">
<style>
  :root {
    --page-bg: #e4e5e8;
    --card-bg: #d3d7de;
    --banner-red: #d2232a;
    --bar-black: #231f20;
    --service-blue: #2b5fb4;
    --ink: #111111;
    --white: #ffffff;
    --art-olive: #d6da72;
    --art-grey: #c3c8d0;
  }
  * { margin: 0; padding: 0; box-sizing: border-box; }
  html, body {
    width: 1200px;
    height: 800px;
    overflow: hidden;
    background: var(--page-bg);
  }
  .business-card {
    position: absolute;
    left: 75px;
    top: 98px;
    width: 1050px;
    height: 605px;
    background: var(--card-bg);
    overflow: hidden;
  }
  .name-banner {
    position: absolute;
    left: 0;
    top: 0;
  }
  .company-name {
    position: absolute;
    left: 63px;
    top: 52px;
    font-family: "Source Serif 4", "Times New Roman", serif;
    font-weight: 700;
    font-size: 56px;
    letter-spacing: -1px;
    color: var(--white);
    line-height: 1;
    white-space: nowrap;
  }
  .accent-bar {
    position: absolute;
    left: 0;
    top: 178px;
    width: 44px;
    height: 227px;
    background: var(--bar-black);
  }
  .services {
    position: absolute;
    left: 64px;
    top: 170px;
    list-style: none;
    font-family: "Arimo", Arial, sans-serif;
    font-style: italic;
    font-weight: 700;
    font-size: 37px;
    line-height: 50px;
    color: var(--service-blue);
  }
  .services li + li { margin-top: 47px; }
  .established {
    position: absolute;
    left: 63px;
    top: 552px;
    font-family: "Arimo", Arial, sans-serif;
    font-weight: 700;
    font-size: 27px;
    color: var(--ink);
    line-height: 1;
  }
  .character-art {
    position: absolute;
    left: 433px;
    top: 162px;
    width: 500px;
    height: 420px;
    background: radial-gradient(ellipse at 55% 55%, var(--art-olive) 0%, var(--art-olive) 45%, var(--art-grey) 100%);
  }
  .speech-bubble {
    position: absolute;
    left: 770px;
    top: 110px;
    width: 260px;
    height: 200px;
  }
  .speech-text {
    position: absolute;
    left: 793px;
    top: 160px;
    width: 220px;
    text-align: center;
    font-family: "Arimo", Arial, sans-serif;
    font-style: italic;
    font-size: 32px;
    line-height: 38px;
    color: var(--ink);
  }
</style>
</head>
<body>
  <section class="business-card">
    <svg class="name-banner" width="830" height="127" viewBox="0 0 830 127" aria-hidden="true">
      <polygon points="0,0 827,0 695,127 0,127" fill="var(--banner-red)"/>
    </svg>
    <h1 class="company-name">TAX PREPARATION CO.</h1>

    <div class="accent-bar"></div>
    <ul class="services">
      <li>INCOME &amp;<br>SALES TAXES</li>
      <li>ELECTRONIC<br>FILING</li>
    </ul>
    <p class="established">ESTABLISHED IN 1993</p>

    <div class="character-art" role="img" aria-label="Illustration of a puzzled woman with a headset seated at a desk, pen over a tax form, against an olive-green square"></div>

    <svg class="speech-bubble" width="260" height="200" viewBox="0 0 260 200" aria-hidden="true">
      <path d="M70,130 L40,185 L100,145 Z" fill="var(--white)" stroke="var(--ink)" stroke-width="2" stroke-linejoin="round"/>
      <ellipse cx="132" cy="87" rx="109" ry="70" fill="var(--white)" stroke="var(--ink)" stroke-width="2"/>
      <path d="M66,138 L98,143" stroke="var(--white)" stroke-width="6"/>
    </svg>
    <p class="speech-text">I'm in over<br>my head</p>
  </section>
</body>
</html>
```